Business Card Design Project

We need a business card design for a new construction company called 'KVORA HOLDINGS PTY.LTD' We run a construction based company for high end market homes in melbourne, we want something that looks professional and eye catching.The card needs to have a strong design to it something modern as the company name explains "kvora." The final design should communicate professionalism and a strong image to our customers on the quality of our work.
On the business card i need
Name: Marek Tollaway
Mob:0417295041
Email:kvora.holdings@mailbrook.example
Domestic/Residential/Commercial
Industry/Entity Type
Construction
Look and feel
Each slider illustrates characteristics of the customer's brand and the style your logo design should communicate.

```html
<!DOCTYPE html>
<html lang="en">
<head>
<meta charset="utf-8">
<title>Kvora Holdings – Business Card</title>
<link rel="stylesheet" href="https://fonts.googleapis.com/css2?family=Michroma&family=Arimo:wght@400&display=swap">
<style>
  :root {
    --backdrop: #c6c7c9;
    --card-white: #ffffff;
    --card-dark: #231f20;
    --brand-red: #e2001a;
    --ink: #231f20;
    --light-text: #ffffff;
  }
  * { box-sizing: border-box; margin: 0; padding: 0; }
  html, body {
    width: 1200px; height: 413px; overflow: hidden;
    background: var(--backdrop);
  }
  .canvas { position: relative; width: 1200px; height: 413px; }

  .card {
    position: absolute; top: 61px;
    width: 520px; height: 288px;
    border-radius: 28px; overflow: hidden;
  }
  .card--front { left: 66px; background: var(--card-white); }
  .card--back { left: 616px; background: var(--card-dark); }

  .company-name {
    position: absolute; left: 0; right: 0;
    text-align: center; white-space: nowrap;
    font-family: "Michroma", sans-serif; font-weight: 400;
    color: var(--ink); line-height: 1;
  }
  .card--front .company-name { top: 132px; font-size: 20px; }
  .card--back .company-name { top: 138px; font-size: 13px; }

  .holder {
    position: absolute; left: 46px; top: 32px;
    font-family: "Michroma", sans-serif; font-size: 17px; line-height: 23px;
    color: var(--light-text);
  }
  .contact {
    position: absolute; left: 251px; top: 45px;
    font-family: "Arimo", sans-serif; font-size: 12.5px; line-height: 17px;
    color: var(--light-text); list-style: none; white-space: nowrap;
  }

  .band { position: absolute; left: 0; top: 99px; width: 520px; height: 91px; }

  .services {
    position: absolute; left: 0; right: 0; top: 243px; text-align: center;
    font-family: "Michroma", sans-serif; font-size: 11.5px;
    color: var(--light-text); white-space: nowrap;
  }
</style>
</head>
<body>
<main class="canvas">
  <section class="card card--front" aria-label="Card front">
    <p class="company-name">KVORA HOLDINGS PTY.LTD</p>
  </section>

  <section class="card card--back" aria-label="Card back">
    <p class="holder">Marek<br>Tollaway</p>
    <ul class="contact">
      <li>M: 0417295041</li>
      <li>E: kvora.holdings@mailbrook.example</li>
    </ul>

    <svg class="band" viewBox="0 0 520 91" aria-hidden="true">
      <polygon points="0,0 501,0 520,45.5 501,91 0,91" fill="var(--card-white)"/>
      <rect x="0" y="31" width="99" height="29" fill="var(--brand-red)"/>
    </svg>

    <p class="company-name">KVORA HOLDINGS PTY.LTD</p>

    <p class="services">Domestic | Residential | Commercial</p>
  </section>
</main>
</body>
</html>
```